Pipelining Product Supply Company Needs New Stationery

We need new stationery (letter head, with compliments slips & business card) for our industry leading pipe lining supply company. basically we sell product to other plumbers to carry out pipe relining.

Im looking for something, fresh, professional, sleek and modern at the same time.

Ive attached a copy of the logo and also some guidelines to follow for colours and fonts etc.

Target Market(s)

Plumbers

Industry/Entity Type

Plumbing

Font styles to use
Sans Serif

Requirements
Must have
• The logo, space for ABN, Address, Phone Number, website and email.
Nice to have
• Stand out from the crowd. To look sleep and professional.
Should not have
• Any other colours apart from what is on the guidelines.

```html
<!DOCTYPE html>
<html lang="en">
<head>
<meta charset="utf-8">
<title>Harbour Reline Supplies – Stationery</title>
<link rel="stylesheet" href="https://fonts.googleapis.com/css2?family=Jost:wght@400;500;700&display=swap">
<style>
  :root {
    --ink: #111111;
    --green: #8dc63f;
    --paper: #ffffff;
    --backdrop: #dcdcdc;
    --grey-text: #bdbdbd;
    --font: "Jost", "Helvetica Neue", Arial, sans-serif;
  }
  * { box-sizing: border-box; margin: 0; padding: 0; }
  html, body { width: 1200px; height: 1168px; overflow: hidden; }
  body { background: var(--backdrop); font-family: var(--font); position: relative; }

  .sheet { position: absolute; background: var(--paper); box-shadow: 0 6px 18px rgba(0,0,0,.18); overflow: hidden; }

  .wordmark { color: var(--green); font-weight: 700; letter-spacing: .02em; text-transform: uppercase; line-height: 1; white-space: nowrap; }

  .company-block { border-left: 3px solid var(--green); padding-left: 8px; text-transform: uppercase; }
  .company-name { color: var(--green); font-weight: 700; }
  .company-line { color: var(--paper); font-weight: 500; }

  /* Letterhead */
  .letterhead { left: 520px; top: 146px; width: 620px; height: 877px; }
  .letterhead .header { position: absolute; left: 0; top: 0; width: 100%; height: 118px; background: var(--ink); }
  .letterhead .header-rule { position: absolute; left: 0; top: 118px; width: 100%; height: 7px; background: var(--green); }
  .letterhead .wordmark { position: absolute; left: 32px; top: 48px; font-size: 30px; }
  .letterhead .company-block { position: absolute; right: 32px; top: 24px; width: 250px; }
  .letterhead .company-name { font-size: 12px; margin-bottom: 4px; }
  .letterhead .company-line { font-size: 9.5px; line-height: 1.45; }
  .letterhead .abn { position: absolute; right: 32px; top: 88px; width: 250px; text-align: right; color: var(--paper); font-size: 9px; font-weight: 500; border-bottom: 1px solid #555; padding-bottom: 3px; }
  .letterhead .footer { position: absolute; left: 0; bottom: 48px; width: 100%; height: 100px; background: var(--green); text-align: center; color: var(--paper); padding-top: 18px; }
  .letterhead .phone { font-size: 32px; font-weight: 700; line-height: 1.1; }
  .letterhead .web { font-size: 18px; font-weight: 700; }

  /* Business cards */
  .card { left: 60px; width: 420px; height: 257px; }
  .card-front { top: 146px; background: var(--ink); }
  .card-front .wordmark { position: absolute; left: 0; right: 0; top: 108px; text-align: center; font-size: 36px; }
  .card-back { top: 460px; background: var(--ink); }
  .card-back .company-block { position: absolute; left: 30px; top: 34px; border-left: none; padding-left: 0; }
  .card-back .company-name { font-size: 15px; margin-bottom: 4px; }
  .card-back .company-line { font-size: 11.5px; line-height: 1.6; }
  .card-back .footer { position: absolute; left: 0; bottom: 0; width: 100%; height: 92px; background: var(--green); color: var(--paper); text-align: right; padding: 14px 30px 0 0; }
  .card-back .phone { font-size: 28px; font-weight: 700; line-height: 1.1; }
  .card-back .web { font-size: 16px; font-weight: 700; }

  /* Compliments slip */
  .slip { left: 60px; top: 774px; width: 420px; height: 198px; }
  .slip .header { position: absolute; left: 0; top: 0; width: 100%; height: 62px; background: var(--ink); }
  .slip .header-rule { position: absolute; left: 0; top: 62px; width: 100%; height: 4px; background: var(--green); }
  .slip .wordmark { position: absolute; left: 18px; top: 24px; font-size: 17px; }
  .slip .company-block { position: absolute; right: 18px; top: 9px; text-align: right; border-left: none; padding-left: 0; }
  .slip .company-name { font-size: 8.5px; margin-bottom: 2px; }
  .slip .company-line { font-size: 7px; line-height: 1.45; }
  .slip .contact { position: absolute; right: 18px; top: 74px; text-align: right; color: var(--green); font-weight: 700; }
  .slip .phone { font-size: 19px; line-height: 1.1; }
  .slip .web { font-size: 10px; }
  .slip .greeting { position: absolute; left: 60px; top: 130px; color: var(--green); font-size: 22px; font-weight: 700; text-transform: uppercase; }
</style>
</head>
<body>

  <section class="sheet letterhead" aria-label="Letterhead">
    <div class="header">
      <div class="wordmark">Harbour Reline</div>
      <div class="company-block">
        <p class="company-name">Harbour Reline Supplies Ltd</p>
        <p class="company-line">14 Fernlea Lane Artarmon NSW 2064</p>
        <p class="company-line">Email?</p>
      </div>
      <p class="abn">ABN: 00 123 456 789</p>
    </div>
    <div class="header-rule"></div>
    <div class="footer">
      <p class="phone">1 300 555 018</p>
      <p class="web">www.harbourreline.com.au</p>
    </div>
  </section>

  <section class="sheet card card-front" aria-label="Business card front">
    <div class="wordmark">Harbour Reline</div>
  </section>

  <section class="sheet card card-back" aria-label="Business card back">
    <div class="company-block">
      <p class="company-name">Harbour Reline Supplies Ltd</p>
      <p class="company-line">14 Fernlea Lane Artarmon NSW 2064</p>
      <p class="company-line">ABN: 00 123 456 789</p>
      <p class="company-line">Email?</p>
    </div>
    <div class="footer">
      <p class="phone">1 300 555 018</p>
      <p class="web">www.harbourreline.com.au</p>
    </div>
  </section>

  <section class="sheet slip" aria-label="With compliments slip">
    <div class="header">
      <div class="wordmark">Harbour Reline</div>
      <div class="company-block">
        <p class="company-name">Harbour Reline Supplies Ltd</p>
        <p class="company-line">14 Fernlea Lane Artarmon NSW 2064 &nbsp;Email?</p>
        <p class="company-line">ABN: 00 123 456 789</p>
      </div>
    </div>
    <div class="header-rule"></div>
    <div class="contact">
      <p class="phone">1 300 555 018</p>
      <p class="web">www.harbourreline.com.au</p>
    </div>
    <p class="greeting">With Compliments</p>
  </section>

</body>
</html>
```